Velmor Sports Foundation website

Velmor sports foundation is a charity organisation that assists young athletes and clubs with the financial assistance they need to progress in their sporting career.

The organisation also establishes mentoring programs to community clubs and individuals.
We envision a home page with a horizontal navigation
Contact Us
Donate: A link to a secure payment system
Meet the team: A list of names and images of the board
Lastly the link to donate should be featured prominently and several times along with cues that lead people to find out more
We prefer limited scrolling and would like to see a clean yet modern design

I am unsure if it needs to be coded or not

Target Market(s)

Potential donors, applications for funds, potential affiliates

Industry/Entity Type

Charity

Coding

Coded - Design and coding required

Number of Pages Required

5+ page

Font styles to use
Sans Serif

Colors
3176b5
ec1f27
34a7d7

Requirements
Must have
• emotionally engaging and informative
• motion enabled pictures
• links to donate
• Music
• Enable video uploads
• Large horizontal pictures of young sports players prominently soccer at this stage
• Social media presence
Nice to have
• Live chat
Should not have
• Images that depict poverty

```html
<!DOCTYPE html>
<html lang="en">
<head>
<meta charset="utf-8">
<title>Velmor Sports Foundation</title>
<link href="https://fonts.googleapis.com/css2?family=Open+Sans:wght@400;600;700&family=Hind:wght@400;500&display=swap" rel="stylesheet">
<style>
:root{
  --blue:#0a4fa0;
  --blue-mid:#3176b5;
  --red:#e52227;
  --sky:#34a7d7;
  --grey-bg:#f5f5f5;
  --text:#6a6a6a;
  --nav:#555;
  --footer:#4a4a4a;
  --white:#fff;
}
*{margin:0;padding:0;box-sizing:border-box}
html,body{width:1087px;height:1200px;overflow:hidden;background:var(--white)}
body{position:relative;font-family:"Hind",sans-serif;color:var(--text)}
a{text-decoration:none;color:inherit}

.site-header{position:absolute;left:0;top:0;width:1087px;height:158px}
.brand{position:absolute;left:120px;top:62px;display:flex;align-items:center;gap:10px}
.brand-dot{width:26px;height:26px;border-radius:50%;background:var(--blue)}
.brand-name{font-family:"Open Sans",sans-serif;font-weight:700;font-size:18px;color:var(--blue)}
.search{position:absolute;left:669px;top:45px;width:181px;height:36px;border:1px solid #ccc;border-radius:2px;font-size:12px;color:#666;padding:9px 12px}
.search svg{position:absolute;right:12px;top:11px}
.btn-donate{position:absolute;display:flex;align-items:center;justify-content:center;gap:5px;color:var(--white);font-family:"Open Sans",sans-serif;font-weight:600;font-size:11px;border-radius:2px}
.btn-donate.header{left:866px;top:45px;width:100px;height:36px;background:var(--red)}
.main-nav{position:absolute;top:110px;left:0;width:1087px;font-size:12px;color:var(--nav)}
.main-nav a{position:absolute}
.main-nav .active{color:var(--red)}

.hero{position:absolute;left:0;top:158px;width:1087px;height:398px;background:linear-gradient(180deg,#3a2e24 0%,#5a4a38 35%,#3b4a2a 70%,#6c8a2e 100%)}
.hero-title{position:absolute;right:121px;top:148px;text-align:right;font-family:"Open Sans",sans-serif;font-weight:700;font-size:26px;line-height:32px;color:var(--white)}
.btn-outline{position:absolute;left:719px;top:223px;width:137px;height:36px;border:2px solid var(--white);border-radius:2px;color:var(--white);display:flex;align-items:center;justify-content:center;gap:6px;font-family:"Open Sans",sans-serif;font-size:11px;font-weight:600}
.btn-donate.hero-btn{left:866px;top:223px;width:100px;height:36px;background:var(--blue-mid)}
.slide-arrow{position:absolute;top:188px}

.welcome{position:absolute;left:0;top:556px;width:1087px;height:340px;background:var(--grey-bg)}
.video{position:absolute;left:118px;top:44px;width:407px;height:254px;background:radial-gradient(circle at 55% 40%,#7a1e24 0%,#2b1b26 40%,#0e1a2c 100%)}
.play{position:absolute;left:184px;top:108px}
.welcome-title{position:absolute;left:560px;top:38px;font-family:"Open Sans",sans-serif;font-weight:700;font-size:25px;line-height:30px;color:var(--blue)}
.welcome-sub{position:absolute;left:560px;top:70px;font-family:"Open Sans",sans-serif;font-weight:600;font-size:19px;color:var(--red)}
.welcome-text{position:absolute;left:560px;top:108px;width:406px;font-size:10px;line-height:17.4px;text-align:justify}
.read-more{position:absolute;left:560px;top:262px;width:80px;height:36px;border:1px solid #ccc;font-size:11px;display:flex;align-items:center;justify-content:center;color:#666}

.cards{position:absolute;top:933px;left:0}
.card{position:absolute;top:0;width:279px;height:144px;background:var(--blue);color:var(--white);text-align:center}
.card svg{position:absolute;left:50%;transform:translateX(-50%);top:22px}
.card h3{position:absolute;top:60px;width:100%;font-family:"Open Sans",sans-serif;font-weight:700;font-size:14px}
.card p{position:absolute;top:88px;left:18px;right:18px;font-size:9px;line-height:13px;color:#c9dbf2}

.site-footer{position:absolute;left:0;top:1113px;width:1087px;height:87px;background:var(--footer);color:#ddd;font-size:10px}
.footer-nav{position:absolute;left:120px;top:26px}
.footer-nav span{margin:0 7px}
.copyright{position:absolute;left:120px;top:49px}
.social{position:absolute;top:32px;width:23px;height:23px;border-radius:50%;background:var(--blue-mid)}
.live-chat{position:absolute;left:661px;top:49px;width:206px;height:38px;background:linear-gradient(180deg,#3cb0e0,#2a97c8);color:var(--white);font-family:"Open Sans",sans-serif;font-size:13px;display:flex;align-items:center;padding-left:16px;gap:8px}
</style>
</head>
<body>
<header class="site-header">
  <a class="brand" href="#"><span class="brand-dot"></span><span class="brand-name">Velmor Sports Foundation</span></a>
  <div class="search">Search
    <svg width="12" height="12" viewBox="0 0 12 12"><circle cx="5" cy="5" r="3.8" fill="none" stroke="#555" stroke-width="1.6"/><line x1="8" y1="8" x2="11" y2="11" stroke="#555" stroke-width="1.8"/></svg>
  </div>
  <a class="btn-donate header" href="#"><svg width="10" height="10" viewBox="0 0 10 10"><circle cx="5" cy="5" r="5" fill="#fff"/><path d="M4 3l2.2 2L4 7" stroke="#e52227" stroke-width="1.4" fill="none"/></svg>Donate Now</a>
  <nav class="main-nav">
    <a class="active" style="left:610px">Home</a>
    <a style="left:670px">Program</a>
    <a style="left:742px">Donate</a>
    <a style="left:807px">Meet the Team</a>
    <a style="left:912px">Contact us</a>
  </nav>
</header>

<section class="hero" role="img" aria-label="Two soccer players challenging for the ball in a floodlit stadium">
  <svg class="slide-arrow" style="left:22px" width="14" height="24" viewBox="0 0 14 24"><path d="M12 2L3 12l9 10" stroke="#bbb" stroke-width="3" fill="none"/></svg>
  <svg class="slide-arrow" style="left:1051px" width="14" height="24" viewBox="0 0 14 24"><path d="M2 2l9 10-9 10" stroke="#bbb" stroke-width="3" fill="none"/></svg>
  <h1 class="hero-title">Quisque vestibulum<br>scelerisque quis egestas</h1>
  <a class="btn-outline" href="#"><svg width="10" height="10" viewBox="0 0 10 10"><circle cx="5" cy="5" r="4.2" fill="none" stroke="#fff" stroke-width="1.3"/><path d="M4 3.2v3.6L6.8 5z" fill="#fff"/></svg>Watch this Video</a>
  <a class="btn-donate hero-btn" href="#"><svg width="10" height="10" viewBox="0 0 10 10"><circle cx="5" cy="5" r="5" fill="#fff"/><path d="M4 3l2.2 2L4 7" stroke="#3176b5" stroke-width="1.4" fill="none"/></svg>Donate Now</a>
</section>

<section class="welcome">
  <div class="video" role="img" aria-label="Soccer player in a red shirt holding a ball, seen from behind under stadium lights">
    <svg class="play" width="40" height="40" viewBox="0 0 40 40"><circle cx="20" cy="20" r="19" fill="#fff" stroke="#222" stroke-width="2"/><path d="M16 12v16l12-8z" fill="#222"/></svg>
  </div>
  <h2 class="welcome-title">Welcome to</h2>
  <p class="welcome-sub">Velmor Sports Foundation</p>
  <p class="welcome-text">Duis in ante sed sem posuere lacinia sit amet et ipsum. In vehicula mattis nisi, vitae imperdiet ex facilisis a. Phasellus eget pellentesque felis. Vestibulum in egestas nibh, vulputate fringilla dolor. Vestibulum laoreet, tellus non eleifend tempor, sapien augue maximus tellus, in vehicula mauris sapien eget orci. Etiam ultrices non quam at commodo. Fusce congue posuere tempor. Aenean fermentum ultrices ante, sit amet ullamcorper massa. Nunc odio purus, interdum quis placerat a, facilisis eu nulla. Quisque dictum vehicula dui ac porttitor. Pellentesque semper tempor magna sit amet luctus. Curabitur venenatis, lectus quis suscipit rhoncus, enim ligula vehicula et lacus rutrum.</p>
  <a class="read-more" href="#">Read more</a>
</section>

<section class="cards">
  <div class="card" style="left:119px">
    <svg width="28" height="30" viewBox="0 0 28 30"><rect x="1.5" y="4" width="25" height="24" rx="2" fill="none" stroke="#fff" stroke-width="2"/><rect x="1.5" y="4" width="25" height="6" fill="#fff"/><rect x="7" y="0" width="3" height="7" fill="#fff"/><rect x="18" y="0" width="3" height="7" fill="#fff"/><g fill="#fff"><rect x="5" y="13" width="4" height="3"/><rect x="12" y="13" width="4" height="3"/><rect x="19" y="13" width="4" height="3"/><rect x="5" y="18" width="4" height="3"/><rect x="12" y="18" width="4" height="3"/><rect x="19" y="18" width="4" height="3"/><rect x="5" y="23" width="4" height="3"/><rect x="12" y="23" width="4" height="3"/></g></svg>
    <h3>PROGRAMS</h3>
    <p>Quisque dictum vehicula dui ac porttitor. Pellentesque semper tempor magna sit amet luctus. Curabitur venenatis, lectus quis suscipit rhoncus.</p>
  </div>
  <div class="card" style="left:404px">
    <svg width="32" height="30" viewBox="0 0 32 30"><g fill="#fff"><circle cx="16" cy="7" r="5"/><circle cx="6" cy="10" r="4"/><circle cx="26" cy="10" r="4"/><path d="M7 28c0-8 4-13 9-13s9 5 9 13z"/><path d="M0 24c0-6 3-9 6-9 2 0 3 1 3 1-2 3-3 6-3 8z"/><path d="M32 24c0-6-3-9-6-9-2 0-3 1-3 1 2 3 3 6 3 8z"/></g></svg>
    <h3>MEET THE TEAM</h3>
    <p>Quisque dictum vehicula dui ac porttitor. Pellentesque semper tempor magna sit amet luctus. Curabitur venenatis, lectus quis suscipit rhoncus.</p>
  </div>
  <div class="card" style="left:688px">
    <svg width="28" height="28" viewBox="0 0 28 28"><path d="M6 1l5 6-3 4c2 4 5 7 9 9l4-3 6 5-3 5C12 27 1 16 1 4z" fill="#fff"/></svg>
    <h3>CONTACT US</h3>
    <p>Quisque dictum vehicula dui ac porttitor. Pellentesque semper tempor magna sit amet luctus. Curabitur venenatis, lectus quis suscipit rhoncus.</p>
  </div>
</section>

<footer class="site-footer">
  <nav class="footer-nav">Home<span>|</span>Program<span>|</span>Donate<span>|</span>Meet the Team<span>|</span>Contact us</nav>
  <p class="copyright">Copyright &copy; 2016 &nbsp;Company name. &nbsp;All rights reserved.</p>
  <span class="social" style="left:884px"></span>
  <span class="social" style="left:913px"></span>
  <span class="social" style="left:943px"></span>
  <a class="live-chat" href="#"><svg width="16" height="13" viewBox="0 0 16 13"><ellipse cx="6" cy="5" rx="6" ry="4.5" fill="#fff"/><ellipse cx="10.5" cy="8" rx="5.5" ry="4" fill="#fff" opacity=".85"/></svg>Live Chat with us</a>
</footer>
</body>
</html>
```